R.T.Pell Logging Web design

Our website needs a redesign. We want it to appear professional and easy to navigate. We will be adding videos and pictures to the new website. We do not sell any products on our website. It should be designed for informational purposes. Our company performs timber harvesting and forest management services. Attached is our new company logo.

www.rtpelllogging-example.com if you want to see our current website.

Industry/Entity Type

Graphic Design

Coding

Coded - Design and coding required

```html
<!DOCTYPE html>
<html lang="en">
<head>
<meta charset="utf-8">
<title>R.T.Pell Logging</title>
<link href="https://fonts.googleapis.com/css2?family=Open+Sans:wght@400;600;700;800&family=Lato:wght@400;700&display=swap" rel="stylesheet">
<style>
:root{
  --brown:#5a2e0f;
  --brown-dark:#4a250b;
  --gold:#e3a31b;
  --gold-dark:#c98a0e;
  --cream:#fdf2cf;
  --wood:#c9936a;
  --wood-line:#b27c55;
  --text:#3b2a1e;
  --muted:#7a6a5c;
  --white:#ffffff;
  --head-bg:#fbf8f2;
}
*{box-sizing:border-box;margin:0;padding:0}
html,body{width:1200px;height:2328px;overflow:hidden}
body{font-family:"Lato",sans-serif;color:var(--text);background:var(--white);position:relative}
.wrap{position:absolute;left:142px;width:916px}

/* header */
.site-header{position:absolute;top:0;left:0;width:1200px;height:122px;background:var(--head-bg)}
.brand{top:30px;display:flex;align-items:center;gap:16px}
.brand-mark{width:58px;height:58px;background:var(--gold);border-radius:8px}
.brand-name{font-family:"Open Sans",sans-serif;font-weight:800;font-size:38px;color:var(--brown);letter-spacing:-0.5px}
.estimate{position:absolute;right:142px;top:18px;display:flex;align-items:center;gap:10px;text-align:left}
.estimate small{display:block;font-size:14px;color:var(--muted)}
.estimate strong{font-family:"Open Sans",sans-serif;font-size:26px;color:var(--brown);font-weight:700}
.main-nav{position:absolute;right:142px;top:80px;display:flex;gap:30px;font-family:"Open Sans",sans-serif;font-size:15px;font-weight:600;color:var(--brown)}
.main-nav a{color:inherit;text-decoration:none;padding-bottom:6px}
.main-nav a.active{border-bottom:3px solid var(--gold)}

/* hero */
.hero{position:absolute;top:122px;left:0;width:1200px;height:490px;background:linear-gradient(90deg,var(--gold-dark),var(--gold) 20%,var(--gold) 80%,var(--gold-dark))}
.hero-floor{position:absolute;top:612px;left:0;width:1200px;height:55px;background:repeating-linear-gradient(90deg,var(--wood) 0 118px,var(--wood-line) 118px 121px);box-shadow:inset 0 6px 8px rgba(0,0,0,.15)}
.hero-slide{position:absolute;top:155px;left:142px;width:916px;height:448px;border:6px solid var(--white);border-radius:6px;background:linear-gradient(180deg,#4f6b3a,#6d5a3c 60%,#8a6a48);box-shadow:0 4px 12px rgba(0,0,0,.3)}
.slide-arrow{position:absolute;top:345px;width:56px;height:56px;border-radius:50%;background:rgba(255,255,255,.75);display:flex;align-items:center;justify-content:center}
.slide-arrow.prev{left:110px}.slide-arrow.next{left:1042px}

/* section titles */
.section-title{position:absolute;left:0;width:1200px;text-align:center;font-family:"Open Sans",sans-serif;font-weight:700;font-size:36px;color:var(--brown);text-transform:uppercase}
.section-title::before,.section-title::after{content:"\2605";color:#a7a7a7;font-size:20px;vertical-align:middle;margin:0 14px}

/* services */
.services{top:755px;display:flex;justify-content:space-between}
.service-card{width:288px;height:267px;background:var(--white);box-shadow:0 3px 10px rgba(0,0,0,.2);border:1px solid #e6e6e6;padding:6px}
.service-photo{height:210px}
.service-card h3{font-family:"Open Sans",sans-serif;font-size:13px;font-weight:700;color:#222;padding:17px 6px 0;white-space:nowrap}

/* welcome */
.welcome-band{position:absolute;top:1073px;left:0;width:1200px;height:427px;background:var(--cream)}
.video-frame{position:absolute;top:1117px;left:142px;width:523px;height:326px;background:linear-gradient(160deg,#4d6a42,#8a7650 60%,#b76b2a);box-shadow:0 3px 10px rgba(0,0,0,.3)}
.video-bar{position:absolute;left:0;right:0;height:30px;background:rgba(0,0,0,.75);color:#fff;font-size:12px;display:flex;align-items:center;padding:0 10px}
.video-bar.top{top:0}.video-bar.bottom{bottom:0}
.video-progress{flex:1;height:4px;background:#666;margin:0 10px;position:relative}
.video-progress span{position:absolute;left:0;top:0;height:4px;width:45%;background:#cc2020}
.play{position:absolute;left:230px;top:135px;width:62px;height:44px;border-radius:10px;background:rgba(30,30,30,.8);display:flex;align-items:center;justify-content:center}
.welcome-text{position:absolute;top:1118px;left:703px;width:355px}
.welcome-text h2{font-family:"Open Sans",sans-serif;font-weight:700;font-size:26px;line-height:1.3;color:var(--brown);margin-bottom:14px}
.welcome-text p{font-size:14px;line-height:20.5px;text-align:justify;color:var(--text)}
.btn-video{position:absolute;top:1386px;left:706px;width:200px;height:48px;background:linear-gradient(180deg,#f2b73d,var(--gold-dark));border:3px solid var(--white);border-radius:6px;box-shadow:0 2px 6px rgba(0,0,0,.3);color:var(--white);font-family:"Open Sans",sans-serif;font-weight:600;font-size:18px;display:flex;align-items:center;justify-content:center}

/* gallery */
.gallery{top:1593px;display:grid;grid-template-columns:repeat(5,160px);gap:26px 29px}
.gallery-item{height:171px;background:var(--white);border-radius:10px;box-shadow:0 2px 8px rgba(0,0,0,.25);padding:7px}
.gallery-item div{height:100%;border-radius:6px}

/* newsletter band */
.signup-band{position:absolute;top:2009px;left:0;width:1200px;height:249px;background:var(--brown)}
.divider{position:absolute;top:0;left:0}
.band-title{position:absolute;font-family:"Open Sans",sans-serif;font-weight:700;font-size:26px;line-height:1.2;color:var(--white);text-align:center;text-transform:uppercase}
.email-field{position:absolute;top:2113px;left:162px;width:360px;height:46px;background:var(--white);border-radius:4px;padding:0 18px;display:flex;align-items:center;color:#888;font-size:16px}
.subscribe-btn{position:absolute;top:2178px;left:235px;width:214px;height:36px;background:var(--gold);border-radius:4px;color:var(--white);font-family:"Open Sans",sans-serif;font-weight:700;font-size:13px;display:flex;align-items:center;justify-content:center;text-transform:uppercase}
.social{position:absolute;top:2155px;left:740px;display:flex;gap:18px}
.social span{width:50px;height:50px;border-radius:50%;background:#e9d9c4}

/* footer */
.site-footer{position:absolute;top:2258px;left:0;width:1200px;height:70px;background:var(--white)}
.footer-icons{position:absolute;left:142px;top:0;width:208px;height:70px;background:var(--gold);display:flex;align-items:center;justify-content:space-around}
.footer-icons span{width:48px;height:48px;border-radius:50%;border:3px solid var(--white);display:flex;align-items:center;justify-content:center}
.footer-nav{position:absolute;left:375px;top:25px;display:flex;gap:16px;font-size:14px;color:var(--brown)}
.copyright{position:absolute;right:142px;top:16px;text-align:right;font-size:15px;color:#333;line-height:1.3}
.copyright em{font-size:13px;color:var(--muted)}
</style>
</head>
<body>

<header class="site-header">
  <div class="wrap brand">
    <div class="brand-mark"></div>
    <div class="brand-name">R.T. PELL LOGGING</div>
  </div>
  <div class="estimate">
    <svg width="30" height="34" viewBox="0 0 30 34"><rect x="1" y="1" width="28" height="32" rx="4" fill="#555"/><rect x="6" y="6" width="18" height="8" fill="#ddd"/><g fill="#ddd"><circle cx="9" cy="20" r="2"/><circle cx="15" cy="20" r="2"/><circle cx="21" cy="20" r="2"/><circle cx="9" cy="26" r="2"/><circle cx="15" cy="26" r="2"/><circle cx="21" cy="26" r="2"/></g></svg>
    <div><small>Call for a Free Estimate</small><strong>(555) 214-3870</strong></div>
  </div>
  <nav class="main-nav">
    <a class="active" href="#">HOME</a><a href="#">ABOUT US</a><a href="#">SERVICES</a><a href="#">LOCATION</a><a href="#">CONTACT US</a>
  </nav>
</header>

<section class="hero"></section>
<div class="hero-floor"></div>
<div class="hero-slide" role="img" aria-label="Forest road with felled logs and a skidder among tall trees"></div>
<div class="slide-arrow prev"><svg width="20" height="24"><path d="M14 3 L5 12 L14 21" stroke="#888" stroke-width="4" fill="none"/></svg></div>
<div class="slide-arrow next"><svg width="20" height="24"><path d="M6 3 L15 12 L6 21" stroke="#888" stroke-width="4" fill="none"/></svg></div>

<h2 class="section-title" style="top:688px">Our Services</h2>
<div class="wrap services">
  <article class="service-card">
    <div class="service-photo" role="img" aria-label="Forestry worker in a helmet thinning a tree plantation" style="background:linear-gradient(160deg,#8aa86a,#5c7a3e 60%,#a0552a)"></div>
    <h3>PLANTATION THINNING</h3>
  </article>
  <article class="service-card">
    <div class="service-photo" role="img" aria-label="Chainsaw cutting a log with sawdust flying" style="background:linear-gradient(160deg,#6b6a58,#9b8a6e 55%,#c9b48f)"></div>
    <h3>TIMBER HARVESTING CUT</h3>
  </article>
  <article class="service-card">
    <div class="service-photo" role="img" aria-label="Log loader machine stacking timber beside a forest" style="background:linear-gradient(180deg,#a9c7dc,#6c8a4a 55%,#9a6e42)"></div>
    <h3>MECHANICAL FELLING &amp; DELIMBING</h3>
  </article>
</div>

<section class="welcome-band"></section>
<div class="video-frame" role="img" aria-label="Video of a logging crew member in a hard hat and safety vest in the forest">
  <div class="video-bar top">R. T. Pell Logging employees also take pride in keeping our customer's forest healthy</div>
  <div class="play"><svg width="20" height="22"><path d="M2 1 L19 11 L2 21Z" fill="#fff"/></svg></div>
  <div class="video-bar bottom">&#9654;&nbsp; 0:07 / 2:13<div class="video-progress"><span></span></div>&#9881;</div>
</div>
<div class="welcome-text">
  <h2>WELCOME TO R. T. PELL</h2>
  <p>Receive high-quality professional logging and land clearing services, from R.T. Pell Logging Company based in Pine Hollow, TX. Whether your tract is large or small, our team of experts can provide the resources and solutions you need to get the job done right. Our track record for consistency, timely service, and expertise will continue to keep us competitive in the East Texas timber industry. We pay top dollar for your pine and hardwood timber.</p>
</div>
<div class="btn-video">Watch Our Video</div>
<svg style="position:absolute;left:668px;top:1424px" width="60" height="50"><path d="M42 10 Q32 45 5 32" stroke="#555" stroke-width="2" stroke-dasharray="4 4" fill="none"/><path d="M5 32 L14 28 M5 32 L11 40" stroke="#555" stroke-width="2"/></svg>

<h2 class="section-title" style="top:1528px">Photo Gallery</h2>
<div class="wrap gallery">
  <div class="gallery-item"><div role="img" aria-label="Harvester head gripping a log" style="background:linear-gradient(160deg,#5b7a3a,#c9a21e)"></div></div>
  <div class="gallery-item"><div role="img" aria-label="Forester in a hard hat holding a tablet" style="background:linear-gradient(160deg,#8fb0c8,#7a8f55)"></div></div>
  <div class="gallery-item"><div role="img" aria-label="Worker felling a tree with a chainsaw" style="background:linear-gradient(160deg,#4f6e3a,#8a5a2c)"></div></div>
  <div class="gallery-item"><div role="img" aria-label="Close view of a yellow harvester head" style="background:linear-gradient(160deg,#3e5a2a,#d7ae1f)"></div></div>
  <div class="gallery-item"><div role="img" aria-label="Chainsaw cutting into a trunk" style="background:linear-gradient(160deg,#6d7a5a,#b25a22)"></div></div>
  <div class="gallery-item"><div role="img" aria-label="Stacked cut logs ends" style="background:linear-gradient(160deg,#c98f48,#8a5a2a)"></div></div>
  <div class="gallery-item"><div role="img" aria-label="Worker with chainsaw among trees" style="background:linear-gradient(160deg,#5a6e44,#b4a06c)"></div></div>
  <div class="gallery-item"><div role="img" aria-label="Pile of branches and logs" style="background:linear-gradient(160deg,#7a5a44,#b89478)"></div></div>
  <div class="gallery-item"><div role="img" aria-label="Forestry worker in safety vest beside log pile" style="background:linear-gradient(160deg,#a28a68,#d8722a)"></div></div>
  <div class="gallery-item"><div role="img" aria-label="Loader moving logs at a timber yard" style="background:linear-gradient(180deg,#b8cfe0,#c9a35a)"></div></div>
</div>

<section class="signup-band">
  <svg class="divider" width="1200" height="249"><path d="M640 0 L560 249" stroke="#6e3c18" stroke-width="3"/></svg>
</section>
<h2 class="band-title" style="top:2040px;left:162px;width:360px">Newsletter<br>Subscription</h2>
<div class="email-field">Email address</div>
<div class="subscribe-btn">Subscribe to Newsletter</div>
<h2 class="band-title" style="top:2040px;left:700px;width:330px">Help Us<br>Spread the Word</h2>
<div class="social" aria-label="Social links"><span></span><span></span><span></span><span></span></div>

<footer class="site-footer">
  <div class="footer-icons">
    <span><svg width="22" height="26"><path d="M11 25 C4 15 2 12 2 9 A9 9 0 0 1 20 9 C20 12 18 15 11 25Z" fill="none" stroke="#fff" stroke-width="2.5"/><circle cx="11" cy="9" r="3" fill="#fff"/></svg></span>
    <span><svg width="24" height="24"><path d="M5 2 L10 2 L11 7 L8 9 Q10 15 15 16 L17 13 L22 14 L22 19 Q21 22 18 22 Q4 20 2 6 Q2 3 5 2Z" fill="#fff"/></svg></span>
    <span><svg width="26" height="20"><path d="M2 7 L13 1 L24 7 L24 19 L2 19Z M2 7 L13 13 L24 7" fill="none" stroke="#fff" stroke-width="2.2"/></svg></span>
  </div>
  <nav class="footer-nav"><span>Home</span><span>About Us</span><span>Contact Us</span><span>Location</span><span>Services</span></nav>
  <div class="copyright">© 2014 RTP<br><em>All rights reserved.</em></div>
</footer>

</body>
</html>
```